Dale Morrikan Plumbing and Heating

Need a card design for a plumbing and heating company that does service and repair, remodels, and plumbing in new construction. Please add following on back side of card; Boilers, Water heaters, Gas lines, Sump pumps, Toilet repairs, Faucet repairs, Pipe thawing, Radiant heating, New construction, Remodels.

Industry/Entity Type

Plumber

Contact Information for Business Card

Was thinking white gloss card with colored logo in middle or black glossy card with silver logo in middle. Just a thought but very open to other designs.

Requirements
Must have
• Need following on front of card;
• P(203) 321-8689
• C(203) 232-9069
• Dale Morrikan 275 Larkwell St West, Stamford, Ct 06214
• service@DrainHearth.example (plumbing in blue, heating in red)
• www.DrainHearth.example (plumbing in blue, heating in red)
• Fully Licensed and Insured
Nice to have
• Elegant design

```html
<!DOCTYPE html>
<html lang="en">
<head>
<meta charset="utf-8">
<title>Dale Morrikan Plumbing and Heating – Business Card</title>
<link rel="stylesheet" href="https://fonts.googleapis.com/css2?family=Open+Sans:wght@400;600;700&display=swap">
<style>
  :root {
    --stage: #2b2d31;
    --card-white: #ffffff;
    --card-shade: #eef0f2;
    --blue-top: #3a8fdc;
    --blue-bottom: #2547b0;
    --brand-blue: #1f5fb8;
    --brand-red: #c8202a;
    --ink: #1d1d1f;
    --rule: #6aa6de;
    --white: #ffffff;
  }
  * { box-sizing: border-box; margin: 0; padding: 0; }
  html, body { width: 1200px; height: 864px; overflow: hidden; }
  body {
    background: var(--stage);
    font-family: "Open Sans", Arial, sans-serif;
    position: relative;
  }
  .card {
    position: absolute;
    left: 300px;
    width: 600px;
    height: 342px;
    border-radius: 3px;
    overflow: hidden;
  }

  /* Back side */
  .card--back {
    top: 56px;
    background: linear-gradient(180deg, var(--blue-top) 0%, var(--blue-bottom) 100%);
    color: var(--white);
    text-align: center;
  }
  .back-brand {
    margin-top: 78px;
    font-weight: 700;
    text-transform: uppercase;
    line-height: 1.1;
  }
  .back-brand__name { display: block; font-size: 26px; letter-spacing: 2px; }
  .back-brand__trade { display: block; font-size: 18px; letter-spacing: 3px; }
  .back-rule {
    width: 330px;
    height: 1px;
    background: rgba(255,255,255,0.7);
    margin: 6px auto 0;
  }
  .back-url { font-size: 12px; font-weight: 700; margin-top: 3px; }
  .service-list {
    list-style: none;
    margin-top: 22px;
    font-size: 16px;
    font-weight: 600;
    line-height: 26px;
  }
  .service-list li { white-space: nowrap; }

  /* Front side */
  .card--front {
    top: 450px;
    background: linear-gradient(160deg, var(--card-white) 55%, var(--card-shade) 100%);
    color: var(--ink);
  }
  .front-brand {
    position: absolute;
    left: 40px;
    top: 48px;
    display: flex;
    align-items: center;
    gap: 12px;
  }
  .brand-dot {
    width: 34px; height: 34px;
    border-radius: 50%;
    background: var(--brand-blue);
  }
  .brand-name {
    font-weight: 700;
    text-transform: uppercase;
    color: var(--brand-blue);
    line-height: 1.15;
  }
  .brand-name__name { display: block; font-size: 20px; letter-spacing: 1.5px; }
  .brand-name__trade { display: block; font-size: 15px; letter-spacing: 2.5px; }
  .owner-name {
    position: absolute;
    right: 40px;
    top: 146px;
    font-size: 20px;
    font-weight: 600;
    color: var(--brand-blue);
  }
  .contact-list {
    position: absolute;
    right: 40px;
    top: 188px;
    list-style: none;
    font-size: 14px;
    line-height: 23px;
  }
  .contact-list li { display: flex; justify-content: flex-end; align-items: center; gap: 10px; }
  .contact-list svg { width: 13px; height: 13px; fill: none; stroke: var(--brand-blue); stroke-width: 2; flex: none; }
  .hl-blue { color: var(--brand-blue); }
  .hl-red { color: var(--brand-red); }
  .rule-line {
    position: absolute;
    height: 1px;
    background: var(--rule);
  }
  .rule-line--left { left: 0; top: 256px; width: 190px; }
  .rule-line--right { left: 300px; right: 0; top: 312px; }
  .tagline {
    position: absolute;
    left: 36px;
    top: 266px;
    font-size: 20px;
    font-weight: 600;
    color: var(--brand-blue);
    white-space: nowrap;
  }
</style>
</head>
<body>
  <section class="card card--back" aria-label="Card back">
    <div class="back-brand">
      <span class="back-brand__name">Dale Morrikan</span>
      <span class="back-brand__trade">Plumbing and Heating</span>
    </div>
    <div class="back-rule"></div>
    <div class="back-url">www.DrainHearth.example</div>
    <ul class="service-list">
      <li>Boilers | Water heaters | Gas lines | Sump pumps | Toilet repairs</li>
      <li>| Faucet repairs | Pipe thawing | Radiant heating</li>
      <li>New construction | Remodels</li>
    </ul>
  </section>

  <section class="card card--front" aria-label="Card front">
    <div class="front-brand">
      <span class="brand-dot"></span>
      <span class="brand-name">
        <span class="brand-name__name">Dale Morrikan</span>
        <span class="brand-name__trade">Plumbing and Heating</span>
      </span>
    </div>

    <div class="owner-name">Dale Morrikan</div>

    <ul class="contact-list">
      <li>(203) 555-0147
        <svg viewBox="0 0 16 16"><path d="M3 2l3 0 1 4-2 1a9 9 0 0 0 4 4l1-2 4 1 0 3c-6 1-12-5-11-11z"/></svg></li>
      <li>(203) 555-0183
        <svg viewBox="0 0 16 16"><rect x="4" y="1" width="8" height="14" rx="1.5"/><line x1="7" y1="12.5" x2="9" y2="12.5"/></svg></li>
      <li><span>service@<span class="hl-blue">Drain</span><span class="hl-red">Hearth</span>.example</span>
        <svg viewBox="0 0 16 16"><rect x="1" y="3" width="14" height="10"/><polyline points="1,3 8,9 15,3"/></svg></li>
      <li><span>www.<span class="hl-blue">Drain</span><span class="hl-red">Hearth</span>.example</span>
        <svg viewBox="0 0 16 16"><path d="M7 9a3 3 0 0 0 4 0l3-3a3 3 0 0 0-4-4l-1 1"/><path d="M9 7a3 3 0 0 0-4 0l-3 3a3 3 0 0 0 4 4l1-1"/></svg></li>
    </ul>

    <div class="rule-line rule-line--left"></div>
    <div class="tagline">Fully Licensed and Insured</div>
    <div class="rule-line rule-line--right"></div>
  </section>
</body>
</html>
```